Business Card Design using new attached logo

We are a family run Plumbing and Heating firm looking to improve our company image with an improved business card and new logo.We are looking to keep the company colour (Blue) involved in our design

Reason: New logo added which needs to be incorporated on designs

Industry/Entity Type

Business

Contact Information for Business Card

See attachment of all info required.

Requirements
Must have
• We have just picked a new company logo which is attached.
• Could you please provide your business card designs using this logo.
• We are looking for the logo on the back as well as the front with all the info required

```html
<!DOCTYPE html>
<html lang="en">
<head>
<meta charset="utf-8">
<title>Kestrel Heating Ltd – Business Card</title>
<link rel="stylesheet" href="https://fonts.googleapis.com/css2?family=Tinos:wght@400;700&display=swap">
<style>
  :root {
    --navy: #0f2140;
    --navy-text: #1b2d4f;
    --paper: #f7f7f5;
    --ink-grey: #5a5f68;
    --rule: #b9bcc2;
    --backdrop: #3b342d;
    --white: #ffffff;
  }
  * { box-sizing: border-box; margin: 0; padding: 0; }
  html, body {
    width: 1200px; height: 781px; overflow: hidden;
    background: var(--backdrop);
    font-family: "Tinos", "Times New Roman", serif;
  }
  .stage {
    width: 1200px; height: 781px;
    display: flex; align-items: center; justify-content: center; gap: 60px;
  }
  .card {
    width: 520px; height: 300px;
    border-radius: 3px;
    box-shadow: 0 12px 30px rgba(0,0,0,.35);
    position: relative;
  }
  /* Front */
  .card--front {
    background: var(--navy);
    display: flex; align-items: center; justify-content: center;
  }
  .wordmark { text-align: center; line-height: 1; }
  .wordmark__name {
    display: block;
    font-size: 54px; letter-spacing: 3px;
  }
  .wordmark__sub {
    display: block;
    font-size: 22px; letter-spacing: 4px; margin-top: 8px;
  }
  .card--front .wordmark { color: var(--white); }

  /* Back */
  .card--back {
    background: var(--paper);
    display: flex; align-items: center;
    padding: 0 30px;
  }
  .card--back .wordmark { color: var(--navy-text); width: 210px; }
  .card--back .wordmark__name { font-size: 38px; letter-spacing: 2px; }
  .card--back .wordmark__sub { font-size: 15px; letter-spacing: 3px; margin-top: 6px; }
  .divider {
    width: 1px; height: 200px; background: var(--rule); margin: 0 26px 0 14px;
  }
  .details { color: var(--ink-grey); font-size: 13px; }
  .person__name {
    color: var(--navy-text); font-weight: 700; font-size: 17px; letter-spacing: 1px;
  }
  .person__role { color: var(--navy-text); font-size: 14px; margin-top: 2px; }
  .details__rule { height: 1px; background: var(--rule); margin: 12px 0; width: 210px; }
  .contact-list { list-style: none; }
  .contact-list li {
    display: flex; align-items: center; gap: 8px; line-height: 1.55;
  }
  .icon { width: 11px; height: 11px; fill: var(--navy-text); flex: none; }
  .address { display: flex; gap: 8px; margin-top: 10px; line-height: 1.4; }
  .address .icon { margin-top: 3px; }
</style>
</head>
<body>
<main class="stage">
  <section class="card card--front" aria-label="Card front">
    <div class="wordmark">
      <span class="wordmark__name">KESTREL</span>
      <span class="wordmark__sub">HEATING LTD</span>
    </div>
  </section>

  <section class="card card--back" aria-label="Card back">
    <div class="wordmark">
      <span class="wordmark__name">KESTREL</span>
      <span class="wordmark__sub">HEATING LTD</span>
    </div>
    <div class="divider"></div>
    <div class="details">
      <p class="person__name">DANIEL HARTLEY</p>
      <p class="person__role">Director</p>
      <div class="details__rule"></div>
      <ul class="contact-list">
        <li><svg class="icon" viewBox="0 0 12 12"><path d="M2 1h3l1 3-1.5 1a6 6 0 0 0 2.5 2.5L8 6l3 1v3a1 1 0 0 1-1 1A9 9 0 0 1 1 2a1 1 0 0 1 1-1z"/></svg>020 7946 0321</li>
        <li><svg class="icon" viewBox="0 0 12 12"><rect x="3" y="0.5" width="6" height="11" rx="1"/><rect x="4" y="2" width="4" height="7" fill="#f7f7f5"/></svg>07700 900412</li>
        <li><svg class="icon" viewBox="0 0 12 12"><rect x="3" y="1" width="6" height="3"/><rect x="1" y="4" width="10" height="5" rx="1"/><rect x="3" y="8" width="6" height="3" fill="#f7f7f5" stroke="#1b2d4f"/></svg>020 7946 0877</li>
        <li><svg class="icon" viewBox="0 0 12 12"><rect x="0.5" y="2" width="11" height="8"/><path d="M1 2.5l5 4 5-4" fill="none" stroke="#f7f7f5"/></svg>daniel@kestrelheating.co.uk</li>
      </ul>
      <div class="address">
        <svg class="icon" viewBox="0 0 12 12"><path d="M6 0a4 4 0 0 1 4 4c0 3-4 8-4 8S2 7 2 4a4 4 0 0 1 4-4z"/><circle cx="6" cy="4" r="1.5" fill="#f7f7f5"/></svg>
        <p>Mill Lane, Ashford<br>Kent TN23 9ZX</p>
      </div>
    </div>
  </section>
</main>
</body>
</html>
```